An international recruitment business looking to attract new engineering and construction clients i

VK Globalis is an international recruitment company with a wealth of experienced engineers, quantity surveyors and construction specialists appropriate to fill roles in the vastly growing Middle East. We need a new, attractive brochure design to send to new clients/companies so they will be interested in our recruitment company and our candidates. We have provided our company logo which we would like to feature, and we would like the theme to match this to some extent. We have also attached our current brochure which should be used for the general content and information. PLEASE NOTE: Ignore the appraisals on the penultimate page - I will provide new ones in a separate document. (Use the one with 5 appraisals, not 3!)
The final design should be modern and attractive and should feature some images of the Middle East including some impressive buildings and new railways (similar to our current ones).
Please also link our website
and use it for inspiration: http://www.vk-globalis.co.uk
Updates
We would like the brochure to be A5 and landscape - although it will only be emailed to clients and not printed.
There is no limit on number of pages.
There seems to be a problem opening the appraisals document I attached.
The content of this document is:
VK Globalis Appraisals
"I had the pleasure of working with VK Globalis as a client and found them to be a great recruiter with in-depth rail knowledge, I had great results from them time after time. I found the team very trustworthy, professional and fun to work with. I would highly recommend VK Globalis and will continue to use the company for all my future recruitment needs"
Tarek Belvedoni, Harbel Transit Company
“When looking to advance my career, I enquired with VK Globalis about a senior position in the Middle East. I dealt specifically with Morven who I found very helpful. He informed me of all the job requirements, the background of the role, responsibilities and package. Morven was extremely diligent in moving the process forward and throughout kept in contact and abreast of the situation. In all it proved a great success and I am now happily placed in my new role. Even though Morven performed beyond the normal boundaries of his role he even now keeps in contact to make sure everything is ok and all parties happy and satisfied with the outcome. I wholeheartedly endorse Morven and VK Globalis and will use them when I am next supplementing my team.”
Ellis Thornbury, Head of Quantity Surveying, Orvane Delta Design Engineers (ODDE), Kuwait
VK Globalis is a recruitment company that has an insatiable appetite for understanding the jobs, for which they recruit, and not only the jobs, but they also establish excellent rapport with the clients and candidates. They are always there when I need to fill positions in my organization quickly. They listen to what I need and always supply me with the resumes that I could review right away to start hiring who I needed - saving me time and effort. They are always able to supply me with the exact person that I need for the open position."
Leila Haddou, HR Consultant, Harbel Lines
Target Market(s)
Professional clients in the Middle East
Industry/Entity Type
Construction
Colors
Designer to choose colors to be used in the design.
Look and feel

```html
<!DOCTYPE html>
<html lang="en">
<head>
<meta charset="utf-8">
<title>VK Globalis – Brochure Pages</title>
<link href="https://fonts.googleapis.com/css2?family=Source+Sans+3:wght@400;600;700&display=swap" rel="stylesheet">
<style>
  :root {
    --stage: #5b5b5b;
    --teal: #17a68b;
    --white: #ffffff;
    --ink: #4a4a4a;
    --ink-soft: #6a6a6a;
    --photo-a: #3a3a3a;
    --photo-b: #bdbdbd;
  }
  * { box-sizing: border-box; margin: 0; padding: 0; }
  html, body { width: 1200px; height: 900px; overflow: hidden; }
  body {
    position: relative;
    background: var(--stage);
    font-family: "Source Sans 3", "Source Sans Pro", Arial, sans-serif;
    color: var(--ink);
  }
  .page {
    position: absolute;
    width: 365px;
    height: 257px;
    background: var(--white);
    overflow: hidden;
  }
  .page > * { z-index: 1; }
  .page--teal { background: var(--teal); color: var(--white); }
  .page--framed { outline: 1px solid #111; }

  .stripe { position: absolute; background: var(--teal); z-index: 0 !important; }
  .band { position: absolute; left: 0; width: 100%; background: var(--teal); z-index: 0 !important; }

  .photo {
    position: absolute;
    z-index: 0 !important;
    background: linear-gradient(160deg, var(--photo-b) 0%, #8a8a8a 45%, var(--photo-a) 100%);
  }

  .brand {
    position: absolute;
    display: flex;
    align-items: center;
    gap: 6px;
    font-weight: 600;
    color: var(--teal);
    white-space: nowrap;
  }
  .brand__dot { border-radius: 50%; background: currentColor; }

  .title {
    position: absolute;
    font-weight: 600;
    color: var(--teal);
    font-size: 14.5px;
    white-space: nowrap;
  }
  .page--teal .title { color: var(--white); }

  .body-copy { position: absolute; font-size: 5.6px; line-height: 1.4; color: var(--ink); }
  .body-copy p + p { margin-top: 6px; }
  .hl { color: var(--teal); font-weight: 700; }

  .bullets { list-style: none; }
  .bullets li { position: relative; padding-left: 12px; }
  .bullets li::before {
    content: ""; position: absolute; left: 0; top: 1px;
    width: 7px; height: 4.5px; border-radius: 3px; background: var(--teal);
  }
  .page--teal .bullets li::before { background: var(--white); }
  .bullets b { font-weight: 700; }

  /* page 3 */
  .service-list { position: absolute; left: 77px; top: 62px; width: 210px; font-size: 5.4px; line-height: 1.38; font-weight: 700; }
  .service-list li + li { margin-top: 7px; }

  /* page 4 & 5 */
  .offer-lead { position: absolute; left: 134px; top: 51px; width: 192px; font-size: 6.4px; line-height: 1.35; text-align: justify; }
  .offer-sub { position: absolute; left: 134px; top: 83px; font-size: 9.5px; font-weight: 700; color: var(--teal); }
  .offer-list { position: absolute; left: 134px; top: 101px; width: 205px; font-size: 5.6px; line-height: 1.4; text-align: justify; }
  .offer-list li + li { margin-top: 6px; }
  .offer-list--cont { left: 49px; top: 51px; width: 200px; }

  /* page 6 */
  .sector-intro { position: absolute; left: 125px; top: 47px; width: 218px; font-size: 5.6px; line-height: 1.35; text-align: justify; }
  .sector { position: absolute; width: 92px; }
  .sector--wide { width: 102px; }
  .sector h3 { font-size: 10px; font-weight: 600; line-height: 1.05; color: var(--ink); }
  .sector p { font-size: 5px; line-height: 1.3; color: var(--ink-soft); margin-top: 1px; }

  /* page 7 */
  .quotes { position: absolute; left: 64px; top: 44px; width: 236px; font-size: 4.9px; line-height: 1.38; font-weight: 700; }
  .quotes blockquote + cite { display: block; text-align: right; font-style: italic; margin: 6px 0 9px; }

  /* page 8 */
  .contact { position: absolute; left: 0; width: 100%; text-align: center; font-size: 4.4px; line-height: 1.45; color: var(--white); }
</style>
</head>
<body>

<!-- Cover -->
<section class="page" style="left:58px; top:55px;">
  <div class="band" style="top:152px; height:105px;"></div>
  <div class="brand" style="left:78px; top:108px; font-size:23px;">
    <span class="brand__dot" style="width:18px; height:18px;"></span>VK Globalis
  </div>
</section>

<!-- Expertise -->
<section class="page" style="left:431px; top:55px;">
  <div class="stripe" style="left:0; top:0; width:52px; height:257px;"></div>
  <div class="photo" role="img" aria-label="Photo of a smiling businesswoman in a dark suit, arms crossed" style="left:18px; top:78px; width:70px; height:179px; border-radius:30px 30px 0 0;"></div>
  <h2 class="title" style="left:134px; width:165px; text-align:center; top:20px;">Expertise</h2>
  <div class="body-copy" style="left:134px; top:47px; width:165px; text-align:center;">
    <p>As a consultancy we pride ourselves in taking full responsibility for providing our clients with the <span class="hl">very best selection of professionals</span> from across the globe.</p>
    <p>We currently recruit <span class="hl">Construction &amp; Engineering Professionals</span> from the UK, EU, Australia, New Zealand, Canada &amp; the USA to work with our prestigious clients across the Middle East.</p>
    <p>Our company prides itself on taking the time and effort involved in <span class="hl">understanding our clients</span>, their needs, their past and most importantly the future of the company and the direction it wishes to take. This information, in turn provides us with the specifications we need to find the talent required for the future of your business.</p>
    <p>We believe that <span class="hl">research</span> is a vital part of keeping ahead. We therefore dedicate part of our business to the continued study of Recruitment Trends, New Developments &amp; Economic Pressures that can have a major effect on where to find and source the best talent needed for you.</p>
  </div>
</section>

<!-- A service like no other -->
<section class="page page--teal" style="left:805px; top:55px;">
  <h2 class="title" style="left:0; width:100%; text-align:center; top:26px;">A service like no other...</h2>
  <ul class="bullets service-list">
    <li>You will benefit from the knowledge and experience of our trained consultants; with an exceptional understanding of the industry sectors as well as the locations and cultures across the Middle East regions.</li>
    <li>We aim to provide “Quality not Quantity” which is the thought process used prior to submitting any candidate to our clients.</li>
    <li>Our aim is to give our clients a full, one stop recruitment service. Using in-depth knowledge of the market, we have the ability to target hard to source professionals for specific positions within your organisation.</li>
    <li>VK Globalis is the next step for your company in ensuring progression &amp; development with the acquisition of highly skilled professionals.</li>
  </ul>
  <svg style="position:absolute; left:290px; top:186px;" width="72" height="72" viewBox="0 0 72 72" aria-hidden="true">
    <circle cx="28" cy="28" r="19" fill="var(--white)"/>
    <line x1="41" y1="41" x2="66" y2="66" stroke="var(--white)" stroke-width="8" stroke-linecap="round"/>
    <path d="M28 18a7 7 0 0 0-4 12.7V34h8v-3.3A7 7 0 0 0 28 18z" fill="none" stroke="var(--teal)" stroke-width="1.8"/>
    <line x1="25" y1="37" x2="31" y2="37" stroke="var(--teal)" stroke-width="1.8"/>
    <line x1="28" y1="11" x2="28" y2="14" stroke="var(--teal)" stroke-width="1.5"/>
    <line x1="17" y1="17" x2="19" y2="19" stroke="var(--teal)" stroke-width="1.5"/>
    <line x1="39" y1="17" x2="37" y2="19" stroke="var(--teal)" stroke-width="1.5"/>
  </svg>
</section>

<!-- What we can offer -->
<section class="page" style="left:58px; top:320px;">
  <div class="stripe" style="left:0; top:0; width:50px; height:257px;"></div>
  <div class="photo" role="img" aria-label="Photo of a businessman in a suit reaching out for a handshake" style="left:10px; top:88px; width:90px; height:169px; border-radius:30px 30px 0 0;"></div>
  <h2 class="title" style="left:134px; top:23px;">What we can offer</h2>
  <p class="offer-lead">We immediately recognise, through experience, that our clients are the most important component to our business.</p>
  <h3 class="offer-sub">Our Services</h3>
  <ul class="bullets offer-list">
    <li><b>CLIENT CENTRED APPROACH</b> - dedicated line management, daily correspondence, speedy feedback and assurance of results.</li>
    <li><b>EXPERT GLOBAL KNOWLEDGE</b> - Major clients and operations across the Globe and majorly in the Gulf Region.</li>
    <li><b>GLOBAL NETWORK</b> - Our international client and candidate network ensures we can resource the top specialists for our clients needs, with current experience from the World’s most prestigious clients and projects.</li>
    <li><b>EMPHASIS ON QUALITY / TARGETTED APPROACH</b> - All candidates presented will be pre-screened and interviewed by our consultants to ensure the highest quality of service.</li>
  </ul>
</section>

<!-- Services continued -->
<section class="page" style="left:431px; top:320px;">
  <div class="stripe" style="left:314px; top:0; width:26px; height:257px;"></div>
  <div class="photo" role="img" aria-label="Photo of an outstretched hand offering a handshake" style="left:219px; top:155px; width:100px; height:64px; border-radius:30px 8px 8px 30px;"></div>
  <ul class="bullets offer-list offer-list--cont">
    <li><b>SEARCH AND SELECTION</b> - The only way to guarantee the best possible talent for the candidates that can’t be found traditionally. Our dedicated head hunting division, guaranteed results.</li>
    <li><b>RECRUITMENT DRIVES</b> - Management of European recruitment events where we can pool in market specialists for volume recruitment. An option for all our valued clients.</li>
    <li><b>EXPERT CONSULTANTS</b> - Our team are leaders in the recruitment field which will provide a proactive, knowledgeable service to our clients.</li>
    <li><b>RESOURCES</b> - We use the most advanced recruitment tools and methods to ensure we remain a distance ahead of our competitors, a position we are proud to retain.</li>
  </ul>
</section>

<!-- Specialist Sectors -->
<section class="page" style="left:805px; top:320px;">
  <div class="stripe" style="left:0; top:0; width:50px; height:257px;"></div>
  <div class="photo" role="img" aria-label="Photo of an engineer in a hard hat holding building plans" style="left:22px; top:160px; width:98px; height:97px; border-radius:34px 34px 0 0;"></div>
  <h2 class="title" style="left:125px; top:23px;">Specialist Sectors</h2>
  <p class="sector-intro">VK Globalis is a consultancy that specialises in the permanent recruitment of professionals within the <span class="hl">Construction &amp; Engineering sector.</span></p>
  <div class="sector" style="left:125px; top:72px;">
    <h3>Architecture</h3>
    <p>New Builds, Regeneration, Conservation, Landscape Architecture, Urban Design, Master planning, Commercial and Redevelopment.</p>
  </div>
  <div class="sector" style="left:125px; top:120px;">
    <h3>Surveying</h3>
    <p>Building Surveying, Land surveying, Quantity Surveying, Rural Practice and Hydrographic Surveying.</p>
  </div>
  <div class="sector sector--wide" style="left:238px; top:73px;">
    <h3>Construction and Building Services</h3>
    <p>Construction Management, Design and Build, Facilities Management and Building Services.</p>
  </div>
  <div class="sector sector--wide" style="left:238px; top:124px;">
    <h3>Civil and Structural Engineering</h3>
    <p>Coastal and Marine, Environmental, Geotechnical, Structural, Highways, Bridges, Rail, Tunnelling, Airports/Ports, Transport planning, Power, Water, Public Health, Risk Management and Project Management.</p>
  </div>
  <div class="sector sector--wide" style="left:238px; top:195px;">
    <h3>Construction and Building Services</h3>
    <p>Construction Management, Design and Build, Facilities Management and Building Services.</p>
  </div>
</section>

<!-- Proven track record -->
<section class="page page--teal" style="left:58px; top:587px;">
  <h2 class="title" style="left:159px; top:17px;">Proven track record...</h2>
  <div class="quotes">
    <blockquote>“Earlier this year I enquired about a senior position in the Middle East. Morven was acting for the employer and was very helpful in confirming their requirements, background and the role, responsibilities and package. Morven was extremely diligent in moving the process forward and throughout kept in contact and abreast of the situation. In all it proved a great success and I am now happily placed in my new role. Even though Morven performed beyond the normal boundaries of his role he even now keeps in contact to make sure everything is ok and all parties happy and satisfied with the outcome. I wholeheartedly endorse Morven and will use him when I next am supplementing my team.”</blockquote>
    <cite>Ellis Thornbury, Head of Quantity Surveying, Orvane Delta Design Engineers (ODDE), Kuwait</cite>
    <blockquote>“I found VK Globalis through a colleague of mine who had used their services in the past. My consultant provided me with various options based on my skills and future requirements. I must say, it has been the easiest recruitment process I have had the pleasure of experiencing. They were very professional and prepared me well for interviews, assisted in my relocation and were very responsive to all my questions and queries. I have no hesitation in recommending VK Globalis to assist in securing the right position for Architects in the Middle East”</blockquote>
    <cite>Maren Ostby, Project Manager, Qasr Almeer Partners, Saudi Arabia</cite>
    <blockquote>“VK Globalis found me a position of a Design Architect for a consultancy in Saudi Arabia. I found them to be a professional recruitment company. Always on hand to answer any queries I had, with a matter of urgency”</blockquote>
    <cite>Ansel Varro, Design Architect, Tellwood &amp; Associates</cite>
  </div>
  <svg style="position:absolute; left:318px; top:203px;" width="46" height="46" viewBox="0 0 46 46" aria-hidden="true">
    <path d="M23 4c11 0 20 7 20 16s-9 16-20 16c-3 0-6-.5-8.5-1.5L4 42l4-10C5 29 3 25 3 20 3 11 12 4 23 4z" fill="none" stroke="var(--white)" stroke-width="2"/>
  </svg>
</section>

<!-- Back cover -->
<section class="page page--framed" style="left:431px; top:587px;">
  <div class="band" style="top:150px; height:107px;"></div>
  <div class="brand" style="left:0; width:100%; justify-content:center; top:190px; font-size:13px; color:var(--white);">
    <span class="brand__dot" style="width:10px; height:10px;"></span>VK Globalis
  </div>
  <div class="contact" style="top:210px;">
    Unit 4, Corran Square, London W1 4QP<br>
    T: 020 7946 0231<br>
    F: 020 7946 0232<br>
    www.vk-globalis.co.uk
  </div>
</section>

</body>
</html>
```